Poster Design Project

We are looking for a poster design to partner with a Parcelwick store. Lindenbrook Media transfers customers photos and videos to DVD and online. Check out our website lindenbrookmedia.example . Basically we are now utilizing Parcelwick as one of our places for customers in New York City to drop off their content. We already have a professional Logo. We would like to incorporate parcelwick and lindenbrook media logo in the poster. The poster size is 12" x 18" We like to stick to a clean look , see our website for details. We want to communicate with customers that they can now drop off their old vhs, hi-8, mini dv and old photos at Parcelwick for transferring to DVD or hard drive.
Updates

Attention: Must use the "The Parcelwick Depot" simple logo not the corporate symbol. 

Reason: We really need an awesome design that is going to be a great seller and super eye catching

WE MUST ONLY USE "THE PARCELWICK DEPOT LOGO" I AM UPLOADING THE IMAGE NOW, IF WE COULD MAKE IT MORE FANCY LIKE HAVE THE BROWN IN THE BACKGROUND WITH THE LETTERS BEING WITH THAT WOULD BE GREAT! 

Target Market(s)

30-100

Industry/Entity Type

Store

Requirements
Must have
• Must use both logos
Must explain clearly the service of VHS to DVD and Photos to DVD
Must be clean/ modern / sleek looking
Nice to have
• Appealing to local new york customers
images of old tapes to dvd
show that it is an easy drop off and pickup situation
fast turnaround
advertise a cheap price of 14.95
Should not have
• not be cheesy

```html
<!DOCTYPE html>
<html lang="en">
<head>
<meta charset="utf-8">
<title>Lindenbrook Media at Parcelwick</title>
<link rel="stylesheet" href="https://fonts.googleapis.com/css2?family=Open+Sans:wght@400;600;700;800&display=swap">
<style>
  :root {
    --sky: #4a90d6;
    --copy-blue: #3a7fc8;
    --page: #ffffff;
    --price-red: #e0211f;
    --parcel-brown: #5b3a1e;
    --parcel-gold: #f2b51c;
    --media-grey: #d9dde2;
    --media-dark: #2f3338;
  }
  html, body {
    margin: 0;
    padding: 0;
    width: 800px;
    height: 1200px;
    overflow: hidden;
    background: var(--page);
  }
  .poster {
    position: relative;
    width: 800px;
    height: 1200px;
    overflow: hidden;
    background: var(--page);
    font-family: "Open Sans", Arial, sans-serif;
  }
  .headline {
    position: absolute;
    top: 26px;
    left: 0;
    width: 800px;
    margin: 0;
    text-align: center;
    color: var(--sky);
    font-weight: 700;
    font-size: 58px;
    line-height: 1.2;
    letter-spacing: -0.5px;
  }
  .hero-photo {
    position: absolute;
    left: 110px;
    top: 180px;
    width: 630px;
    height: 640px;
    background:
      radial-gradient(ellipse 45% 35% at 70% 25%, rgba(214, 206, 236, 0.9), rgba(214, 206, 236, 0) 100%),
      radial-gradient(ellipse 55% 30% at 55% 80%, rgba(190, 40, 40, 0.55), rgba(190, 40, 40, 0) 100%),
      radial-gradient(ellipse 60% 40% at 45% 62%, rgba(40, 40, 44, 0.85), rgba(40, 40, 44, 0) 100%),
      #ffffff;
  }
  .price-badge {
    position: absolute;
    left: 74px;
    top: 240px;
    width: 166px;
    height: 166px;
    border-radius: 50%;
    background: var(--price-red);
    color: #fff;
    display: flex;
    flex-direction: column;
    align-items: center;
    justify-content: center;
    font-weight: 700;
    line-height: 1.12;
    text-align: center;
  }
  .price-badge .label { font-size: 29px; }
  .price-badge .amount { font-size: 33px; }
  .service-copy {
    position: absolute;
    top: 858px;
    left: 0;
    width: 800px;
    margin: 0;
    text-align: center;
    color: var(--copy-blue);
    font-weight: 700;
    font-size: 24px;
    line-height: 1.65;
    white-space: nowrap;
    letter-spacing: -0.2px;
  }
  .brand-row {
    position: absolute;
    top: 1070px;
    left: 0;
    width: 800px;
    height: 110px;
    display: flex;
    justify-content: center;
    align-items: center;
    gap: 70px;
  }
  .brand {
    display: flex;
    align-items: center;
    gap: 14px;
    font-weight: 700;
    font-size: 32px;
    white-space: nowrap;
  }
  .brand-media { color: var(--media-dark); }
  .brand-media .mark {
    width: 70px; height: 70px; border-radius: 50%;
    background: var(--media-grey);
  }
  .brand-parcel { color: var(--parcel-brown); }
  .brand-parcel .mark {
    width: 60px; height: 60px;
    background: var(--parcel-gold);
  }
</style>
</head>
<body>
  <main class="poster">
    <h1 class="headline">Don't lose your<br>precious memories...</h1>

    <div class="hero-photo" role="img" aria-label="Photo of a stack of old VHS and camcorder tapes with a DVD in an open clear case"></div>

    <div class="price-badge">
      <span class="label">Prices<br>from</span>
      <span class="amount">$14.95</span>
    </div>

    <p class="service-copy">Digitize your memories by having your old<br>vhs, hi-8, mini dv and old photos transferred to<br>DVD or hard drive. Simply drop off and pick up at<br>Parcelwick and take advantage of our fast turnaround.</p>

    <div class="brand-row">
      <div class="brand brand-media"><span class="mark"></span>Lindenbrook Media</div>
      <div class="brand brand-parcel"><span class="mark"></span>Parcelwick</div>
    </div>
  </main>
</body>
</html>
```